Website Design for LipoweZacisze.pl – Luxury Wedding Car Rental with Chauffeur

We are looking for a talented designer to create a modern, elegant, and fully responsive website for our new brand – LipowyZacisze.pl. We are a premium car rental platform in Poland, offering luxury and exotic vehicles exclusively for weddings. All cars come with a professional chauffeur, ensuring a high-end, stress-free, and stylish experience.
Website Purpose:
The website should present our offering in a luxurious, clear, and inspiring way. It must build trust, highlight the prestige of our brand, and encourage inquiries. Our target audience includes engaged couples, wedding planners, and clients seeking a truly exceptional vehicle for their special day.
Design Requirements:
Style: modern, elegant, minimalist
Color palette: white, black, gold, optionally silver – refined and luxurious
Typography: clean, modern, high-end
Layout: clear, intuitive, with large car images and well-defined sections
Fully responsive (desktop, tablet, mobile)
Bilingual layout (Polish/English) must be considered
Pages to Design:
Homepage
About Us
Fleet Overview
Individual Car Pages
Services (Weddings, Photo Shoots, Film Rentals)
Why Us / Unique Selling Points
Contact
FAQ
Inspiration:
Luxury automotive brands (e.g. Vellor-Kane, Carrow, Dunmere Vale)
High-end wedding websites
Minimalist layouts with large visuals and elegant typography
Additional Notes:
The design should evoke the emotions of a wedding day – elegance, uniqueness, style, and class. Please avoid flashy colors, excessive graphic effects, or overly decorative elements. Subtlety, prestige, and sophistication are key.

```html
<!DOCTYPE html>
<html lang="en">
<head>
<meta charset="utf-8">
<title>LipoweZacisze.pl – Luxury Wedding Cars</title>
<link href="https://fonts.googleapis.com/css2?family=Cormorant+Garamond:wght@500;600;700&family=Poppins:wght@400;500;600&display=swap" rel="stylesheet">
<style>
:root{
  --gold:#d6b85a;
  --gold-dark:#b99a3e;
  --ink:#1c1c1c;
  --charcoal:#3b3b3b;
  --night:#121212;
  --white:#ffffff;
  --muted:#5a5a5a;
  --serif:'Cormorant Garamond', serif;
  --sans:'Poppins', sans-serif;
}
*{box-sizing:border-box;margin:0;padding:0}
html,body{width:1200px;height:4622px;overflow:hidden}
body{position:relative;background:var(--white);font-family:var(--sans);color:var(--ink)}
.abs{position:absolute}
.serif{font-family:var(--serif);font-weight:600;text-transform:uppercase;letter-spacing:.5px}
.btn{position:absolute;display:flex;align-items:center;justify-content:center;border-radius:30px;font-family:var(--serif);font-weight:700;font-size:11px;text-transform:uppercase;letter-spacing:.4px}
.btn-gold{background:var(--gold);color:var(--ink)}
.btn-line{border:1.5px solid var(--gold);color:var(--white)}
.section-title{position:absolute;left:0;width:1200px;text-align:center;font-family:var(--serif);font-weight:600;font-size:34px;text-transform:uppercase}
.brand{font-family:var(--serif);font-weight:700;color:var(--gold);font-size:22px;display:flex;align-items:center;gap:8px}
.brand i{display:block;width:10px;height:10px;border-radius:50%;background:var(--gold)}
/* hero */
.hero{left:0;top:0;width:1200px;height:592px;background:radial-gradient(ellipse at 72% 45%,#4a4d54 0%,#24262b 40%,#0d0d0f 80%)}
.nav a{position:absolute;top:27px;font-family:var(--serif);font-weight:600;font-size:11px;color:var(--white);text-decoration:none}
.nav a.active{color:var(--gold);text-decoration:underline}
.hero h1{position:absolute;left:122px;top:168px;font-family:var(--serif);font-weight:600;font-size:42px;line-height:56px;color:var(--white)}
.hero p{position:absolute;left:122px;top:277px;width:380px;font-size:11px;line-height:14px;color:var(--white)}
/* fleet */
.fleet{left:0;top:1055px;width:1200px;height:605px;background:linear-gradient(180deg,#2a2420,#1a1715 60%,#2a2622)}
.car-card{position:absolute;top:1178px;width:305px;height:342px;background:var(--white);border-radius:10px;overflow:hidden;text-align:center}
.car-card .ph{height:222px}
.car-card h3{margin-top:16px;font-family:var(--serif);font-weight:600;font-size:17px;text-transform:uppercase}
.car-card p{font-size:11px;color:var(--muted);margin-top:2px}
.car-card .view{margin:14px auto 0;width:100px;height:32px;border-radius:20px;background:var(--gold);display:flex;align-items:center;justify-content:space-between;padding:0 4px 0 14px;font-family:var(--serif);font-weight:700;font-size:10px}
.dot-arrow{width:24px;height:24px;border-radius:50%;background:var(--white);display:flex;align-items:center;justify-content:center}
.nav-arrow{position:absolute;width:44px;height:44px;border-radius:50%;border:1.5px solid var(--gold);display:flex;align-items:center;justify-content:center}
/* services */
.service{position:absolute;top:1783px;width:305px;height:235px;border-radius:10px;overflow:hidden}
.service span{position:absolute;left:20px;bottom:14px;font-family:var(--serif);font-weight:600;font-size:23px;color:var(--white);text-transform:uppercase}
.service b{position:absolute;right:16px;bottom:14px;width:26px;height:26px;border-radius:50%;background:var(--gold);display:flex;align-items:center;justify-content:center}
/* how */
.dark-band{left:0;width:1200px;background:var(--charcoal)}
.step h4{font-family:var(--serif);font-weight:600;font-size:16px;color:var(--white);text-transform:uppercase}
.step p{font-size:11px;line-height:13px;color:#e6e6e6;margin-top:4px}
/* why */
.feat h4{font-family:var(--serif);font-weight:600;font-size:17px;text-transform:uppercase}
.feat p{font-size:11px;color:var(--muted);line-height:13px;margin-top:3px}
.gold-ico{position:absolute;width:86px;height:86px;border-radius:50%;background:var(--gold);border:3px solid var(--white);box-shadow:0 0 0 2px var(--gold);display:flex;align-items:center;justify-content:center}
/* testimonials */
.quote{position:absolute;top:3265px;width:468px;height:190px;border:1px solid var(--gold);border-bottom:5px solid var(--gold);border-radius:12px}
.quote p{position:absolute;left:34px;top:62px;width:405px;font-size:12px;line-height:23px;color:var(--white)}
.quote .stars{position:absolute;left:34px;top:135px;color:var(--gold);font-size:11px;letter-spacing:1px}
.quote .who{position:absolute;left:34px;top:152px;font-size:10px;font-weight:600;color:var(--white)}
.avatar{position:absolute;top:-33px;left:34px;width:66px;height:66px;border-radius:50%;background:linear-gradient(#b7c2cc,#5c6670);border:3px solid var(--gold)}
/* faq */
.faq-item{position:absolute;left:122px;width:468px;height:40px;border:1.5px solid #e6d7a6;border-radius:4px;display:flex;align-items:center;justify-content:space-between;padding:0 12px;font-size:13px}
.faq-item .q{display:flex;align-items:center;gap:6px}
.ring{width:9px;height:9px;border-radius:50%;border:1.5px solid var(--gold)}
/* footer */
.footer{left:0;top:4333px;width:1200px;height:289px;background:var(--night);color:var(--white)}
.fcol h5{font-family:var(--serif);font-weight:600;font-size:14px;text-transform:uppercase;margin-bottom:14px}
.fcol a{display:block;font-size:9px;color:var(--white);text-decoration:none;margin-bottom:12px;text-transform:uppercase}
.contact-row{display:flex;align-items:center;gap:14px;font-size:10px;margin-bottom:14px}
.ico-box{width:22px;height:22px;border-radius:4px;background:var(--gold)}
</style>
</head>
<body>

<!-- HERO -->
<div class="abs hero" role="img" aria-label="Groom and bride beside a black luxury car at night"></div>
<svg class="abs" style="left:0;top:0" width="1200" height="600" viewBox="0 0 1200 600">
  <path d="M0,404 Q560,730 1200,421 L1200,600 L0,600 Z" fill="#ffffff"/>
  <path d="M0,412 Q560,740 1200,428" fill="none" stroke="#d6b85a" stroke-width="3"/>
</svg>
<div class="abs brand" style="left:122px;top:14px"><i></i>LipoweZacisze</div>
<nav class="nav">
  <a class="active" style="left:509px">HOME</a>
  <a style="left:573px">ABOUT US</a>
  <a style="left:658px">FLEET OVERVIEW</a>
  <a style="left:779px">SERVICES</a>
  <a style="left:859px">WHY US</a>
  <a style="left:932px">FAQ</a>
</nav>
<div class="btn btn-gold" style="left:976px;top:16px;width:102px;height:34px">Contact us</div>
<div class="abs" style="left:122px;top:142px;font-family:var(--serif);font-weight:600;font-size:13px;color:var(--white)">WELCOM TO <span style="color:var(--gold);font-size:16px">LipoweZacisze</span></div>
<h1 class="hero-title" style="position:absolute;left:122px;top:168px;font-family:var(--serif);font-weight:600;font-size:42px;line-height:56px;color:#fff">ARRIVE IN ELEGANCE.<br>REMEMBER FOREVER.</h1>
<p class="abs" style="left:122px;top:277px;width:390px;font-size:11px;line-height:14px;color:#fff">Exquisite luxury cars with professional chauffeurs – because your wedding deserves nothing less.</p>
<div class="btn btn-gold" style="left:122px;top:328px;width:118px;height:44px">View our fleet</div>
<div class="btn btn-line" style="left:252px;top:328px;width:122px;height:44px">Get a quote</div>

<!-- ABOUT -->
<svg class="abs" style="left:110px;top:595px" width="400" height="400" viewBox="0 0 400 400">
  <circle cx="190" cy="202" r="190" fill="none" stroke="#d6b85a" stroke-width="1.5"/>
  <path d="M30,90 A175,175 0 0 1 330,70" fill="none" stroke="#d6b85a" stroke-width="1"/>
  <path d="M40,320 A185,185 0 0 0 360,290" fill="none" stroke="#d6b85a" stroke-width="2"/>
</svg>
<div class="abs" role="img" aria-label="Bride and groom beside a vintage white car among trees" style="left:125px;top:615px;width:365px;height:365px;border-radius:50%;background:linear-gradient(160deg,#9bab7c,#d9d4c6 55%,#a89584)"></div>
<div class="abs serif" style="left:629px;top:665px;font-size:34px">About us</div>
<div class="abs" style="left:629px;top:710px;width:450px;font-size:11px;line-height:19px;color:var(--muted)">
  At LipowyZacisze.pl, we believe that a wedding day should feel like a fairytale — from the first glance to the final getaway. Our brand was born from a passion for exceptional automobiles and the magic of celebration. We set out to create a premium car rental experience exclusively for weddings — combining style, sophistication, and impeccable service.
  <br><br>From our very first couple to hundreds of newlyweds across Poland, our mission remains the same:<br><span style="color:var(--ink)">To deliver moments of luxury, comfort, and unforgettable elegance.</span>
</div>
<div class="btn btn-gold" style="left:629px;top:901px;width:111px;height:42px">Learn more</div>

<!-- FEATURED FLEET -->
<div class="abs fleet" role="img" aria-label="Dim close-up of a classic car's grille"></div>
<div class="section-title" style="top:1108px;color:#fff">Featured fleet</div>
<div class="nav-arrow" style="left:56px;top:1328px"><svg width="10" height="14"><path d="M8,1 L2,7 L8,13" fill="none" stroke="#fff" stroke-width="1.5"/></svg></div>
<div class="nav-arrow" style="left:1100px;top:1328px"><svg width="10" height="14"><path d="M2,1 L8,7 L2,13" fill="none" stroke="#fff" stroke-width="1.5"/></svg></div>
<div class="car-card" style="left:122px"><div class="ph" role="img" aria-label="Black luxury SUV front view in dark studio" style="background:linear-gradient(#1f1f22,#3a3a3e 60%,#141416)"></div><h3>Vellor-Kane Sovereign</h3><p>Timeless elegance with unmatched comfort.</p><div class="view">View car<span class="dot-arrow"><svg width="6" height="10"><path d="M1,1 L5,5 L1,9" fill="none" stroke="#000" stroke-width="1.5"/></svg></span></div></div>
<div class="car-card" style="left:447px"><div class="ph" role="img" aria-label="Black sedan parked before a lit hotel entrance" style="background:linear-gradient(#5a4632,#2a2119 60%,#121010)"></div><h3>Carrow Meridian GT</h3><p>Sleek, stylish, and utterly sophisticated.</p><div class="view">View car<span class="dot-arrow"><svg width="6" height="10"><path d="M1,1 L5,5 L1,9" fill="none" stroke="#000" stroke-width="1.5"/></svg></span></div></div>
<div class="car-card" style="left:772px"><div class="ph" role="img" aria-label="Silver vintage limousine in front of a brick building" style="background:linear-gradient(#a9735a,#c7b8a4 55%,#8e8c88)"></div><h3>Halvorsen S-Line Regent</h3><p>Luxury redefined for modern royalty.</p><div class="view">View car<span class="dot-arrow"><svg width="6" height="10"><path d="M1,1 L5,5 L1,9" fill="none" stroke="#000" stroke-width="1.5"/></svg></span></div></div>
<div class="btn btn-gold" style="left:538px;top:1556px;width:124px;height:42px">See full fleet</div>

<!-- SERVICES -->
<div class="section-title" style="top:1712px">Our services</div>
<div class="service" style="left:122px" role="img" aria-label="Bride and groom with a black vintage car"><div style="position:absolute;inset:0;background:linear-gradient(#7d8f6a,#3b3f38 70%,#1c1c1c)"></div><span>Weddings</span><b><svg width="6" height="10"><path d="M1,1 L5,5 L1,9" fill="none" stroke="#000" stroke-width="1.5"/></svg></b></div>
<div class="service" style="left:447px" role="img" aria-label="Couple posing with a white classic car in autumn forest"><div style="position:absolute;inset:0;background:linear-gradient(#8a7a3e,#5e5530 60%,#2a261a)"></div><span>Photo shoots</span><b><svg width="6" height="10"><path d="M1,1 L5,5 L1,9" fill="none" stroke="#000" stroke-width="1.5"/></svg></b></div>
<div class="service" style="left:772px" role="img" aria-label="Couple standing by a white sedan under blue sky"><div style="position:absolute;inset:0;background:linear-gradient(#6d8fc0,#9aa1a6 50%,#2b2b2b)"></div><span>Film rentals</span><b><svg width="6" height="10"><path d="M1,1 L5,5 L1,9" fill="none" stroke="#000" stroke-width="1.5"/></svg></b></div>

<!-- HOW IT WORKS -->
<div class="abs dark-band" style="top:2081px;height:449px"></div>
<div class="section-title" style="top:2133px;color:#fff">How it works</div>
<svg class="abs" style="left:0;top:2190px" width="1200" height="170">
  <path d="M290,80 C360,120 460,110 535,80 M665,80 C760,30 860,30 945,80" fill="none" stroke="#d6b85a" stroke-width="1.2"/>
  <g fill="none" stroke="#d6b85a">
    <circle cx="225" cy="80" r="66" stroke-width="1.2"/><circle cx="225" cy="80" r="58" stroke-width="1"/>
    <circle cx="600" cy="80" r="66" stroke-width="1.2"/><circle cx="600" cy="80" r="58" stroke-width="1"/>
    <circle cx="1010" cy="80" r="66" stroke-width="1.2"/><circle cx="1010" cy="80" r="58" stroke-width="1"/>
  </g>
  <g fill="none" stroke="#ffffff" stroke-width="1.5">
    <path d="M200,92 L202,76 L210,66 L240,66 L248,76 L250,92 Z M200,92 L200,100 M250,92 L250,100"/>
    <circle cx="211" cy="84" r="3"/><circle cx="239" cy="84" r="3"/>
    <circle cx="600" cy="80" r="24"/><circle cx="600" cy="80" r="14"/>
    <circle cx="1010" cy="64" r="7"/><path d="M990,98 L994,84 L1026,84 L1030,98 Z"/><circle cx="1000" cy="98" r="3"/><circle cx="1020" cy="98" r="3"/>
  </g>
</svg>
<div class="abs step" style="left:122px;top:2347px;width:210px;text-align:center"><h4>Choose your dream car</h4><p>Browse our curated collection<br>and find the perfect match.</p></div>
<div class="abs step" style="left:450px;top:2347px;width:300px;text-align:center"><h4>Customize your experience</h4><p>Let us know your wedding details —<br>we'll tailor everything to you.</p></div>
<div class="abs step" style="left:878px;top:2347px;width:200px;text-align:right"><h4>Enjoy the ride</h4><p>Relax. We handle every<br>detail on the day itself.</p></div>
<div class="btn btn-gold" style="left:541px;top:2420px;width:118px;height:43px">Get a quote</div>

<!-- WHY CHOOSE US -->
<div class="section-title" style="top:2580px">Why choose us</div>
<svg class="abs" style="left:0;top:2640px" width="1200" height="420">
  <path d="M440,60 A180,190 0 1 1 470,390" fill="none" stroke="#d6b85a" stroke-width="2"/>
  <path d="M500,40 A190,195 0 0 1 780,340" fill="none" stroke="#d6b85a" stroke-width="1"/>
  <line x1="122" y1="192" x2="390" y2="192" stroke="#e3cf92" stroke-width="1"/>
  <line x1="810" y1="192" x2="1078" y2="192" stroke="#e3cf92" stroke-width="1"/>
</svg>
<div class="abs" role="img" aria-label="Silver hatchback car three-quarter view" style="left:400px;top:2720px;width:390px;height:230px;border-radius:45% 50% 30% 30%;background:radial-gradient(ellipse at 50% 45%,#e9eaec,#b4b7bb 60%,#ffffff 75%)"></div>
<div class="gold-ico" style="left:122px;top:2678px"><svg width="40" height="40" fill="none" stroke="#222" stroke-width="1.6"><rect x="8" y="6" width="24" height="28" rx="3"/><path d="M12,24 L28,24 M14,14 L26,14"/></svg></div>
<div class="abs feat" style="left:217px;top:2700px"><h4>Serving all of Poland</h4><p>Nationwide coverage, local expertise</p></div>
<div class="gold-ico" style="left:992px;top:2678px"><svg width="40" height="40" fill="none" stroke="#222" stroke-width="1.6"><path d="M6,26 L9,16 L31,16 L34,26 Z"/><circle cx="13" cy="28" r="3"/><circle cx="27" cy="28" r="3"/></svg></div>
<div class="abs feat" style="left:700px;top:2694px;width:282px;text-align:right"><h4>Wedding-ready fleet</h4><p>Immaculately prepared<br>inside and out</p></div>
<div class="gold-ico" style="left:122px;top:2908px"><svg width="40" height="40" fill="none" stroke="#222" stroke-width="1.6"><circle cx="20" cy="12" r="5"/><path d="M8,32 L11,22 L29,22 L32,32 Z"/></svg></div>
<div class="abs feat" style="left:217px;top:2932px"><h4>Prestige vehicles only</h4><p>Vellor-Kane, Carrow, Halvorsen, and more</p></div>
<div class="gold-ico" style="left:992px;top:2908px"><svg width="40" height="40" fill="none" stroke="#222" stroke-width="1.6"><circle cx="20" cy="20" r="13"/><circle cx="20" cy="20" r="7"/></svg></div>
<div class="abs feat" style="left:700px;top:2926px;width:282px;text-align:right"><h4>Perfect for photos</h4><p>Iconic vehicles that enhance<br>your wedding album</p></div>

<!-- TESTIMONIALS -->
<div class="abs dark-band" style="top:3100px;height:422px"></div>
<div class="section-title" style="top:3150px;color:#fff">What our&nbsp; client say</div>
<div class="nav-arrow" style="left:56px;top:3335px"><svg width="10" height="14"><path d="M8,1 L2,7 L8,13" fill="none" stroke="#fff" stroke-width="1.5"/></svg></div>
<div class="nav-arrow" style="left:1100px;top:3335px"><svg width="10" height="14"><path d="M2,1 L8,7 L2,13" fill="none" stroke="#fff" stroke-width="1.5"/></svg></div>
<div class="quote" style="left:122px"><div class="avatar" role="img" aria-label="Client portrait"></div><p>"The car arrived early, spotless inside and out, with a courteous chauffeur who made us feel at ease. It wasn't just a ride, it was an experience. Our guests are still talking about the entrance!"</p><div class="stars">★★★★★</div><div class="who">Marta &amp; Tomasz, Wrocław</div></div>
<div class="quote" style="left:610px"><div class="avatar" role="img" aria-label="Client portrait"></div><p>"The car looked amazing in every photo. Our photographer said it was one of the most photogenic arrivals he's ever captured. Thank you for helping create magic."</p><div class="stars">★★★★★</div><div class="who">Ola &amp; Piotr, Łódź</div></div>

<!-- FAQ -->
<div class="section-title" style="top:3573px;font-size:30px">Frequently asked questions</div>
<div class="abs" style="left:122px;top:3640px;width:468px;height:118px;background:var(--gold);border-radius:4px;padding:10px 14px">
  <div style="display:flex;justify-content:space-between;font-size:13px"><span style="display:flex;align-items:center;gap:6px"><span class="ring" style="border-color:#fff"></span>Is chauffeur service included?</span><span>–</span></div>
  <p style="font-size:9.5px;line-height:16px;color:#5b4d21;margin-top:4px;padding-left:15px">Yes — all of our vehicles come with a professionally trained, impeccably dressed chauffeur. Punctual, discreet, and experienced in wedding-day etiquette, your chauffeur ensures every arrival is smooth, elegant, and stress-free — so you can simply enjoy the ride.</p>
</div>
<div class="faq-item" style="top:3778px"><span class="q"><span class="ring"></span>Can I decorate the vehicle?</span><span>+</span></div>
<div class="faq-item" style="top:3836px"><span class="q"><span class="ring"></span>How far in advance should I book?</span><span>+</span></div>
<div class="faq-item" style="top:3893px"><span class="q"><span class="ring"></span>Do you operate nationwide?</span><span>+</span></div>
<div class="faq-item" style="top:3950px"><span class="q"><span class="ring"></span>Can I use the car for a photo shoot only?</span><span>+</span></div>
<div class="abs" role="img" aria-label="Front grille of a vintage wedding car with flowers" style="left:710px;top:3652px;width:365px;height:365px;border-radius:50%;background:radial-gradient(circle at 50% 55%,#b9ad9e,#6f5f50 55%,#4d5a3e)"></div>

<!-- CTA -->
<div class="abs" role="img" aria-label="Floral-decorated wedding car at dusk" style="left:0;top:4036px;width:1200px;height:297px;background:linear-gradient(180deg,#4c3a22,#2a2016 55%,#1a140d)"></div>
<svg class="abs" style="left:0;top:4036px" width="1200" height="120"><path d="M0,0 L1200,0 L1200,55 Q600,-40 0,55 Z" fill="#ffffff"/><path d="M0,55 Q600,-40 1200,55" fill="none" stroke="#d6b85a" stroke-width="2"/></svg>
<div class="section-title" style="top:4130px;color:#fff;font-size:30px">Reserve your wedding car today</div>
<div class="abs" style="left:0;width:1200px;top:4172px;text-align:center;font-size:11px;line-height:13px;color:#fff">Availability is limited – especially during peak wedding season. Secure your<br>dream car with just a few clicks.</div>
<div class="btn btn-gold" style="left:472px;top:4212px;width:138px;height:43px">Check availability</div>
<div class="btn btn-line" style="left:616px;top:4212px;width:110px;height:43px">Contact us</div>

<!-- FOOTER -->
<div class="abs footer"></div>
<div class="abs brand" style="left:122px;top:4365px"><i></i>LipoweZacisze</div>
<p class="abs" style="left:122px;top:4412px;width:190px;font-size:8.5px;line-height:14px;color:#fff">At LipowyZacisze.pl we believe that a wedding day should feel like a fairytale — from the first glance to the final getaway.</p>
<div class="abs fcol" style="left:383px;top:4368px"><h5>Quick links</h5><a>Home</a><a>About us</a><a>Fleet overview</a><a>Services</a><a>Why us</a><a>FAQ</a></div>
<div class="abs fcol" style="left:535px;top:4368px"><h5>Contact info</h5>
  <div class="contact-row"><span class="ico-box"></span>+48 500 214 736</div>
  <div class="contact-row"><span class="ico-box"></span>kontakt@lipowezacisze.pl</div>
  <div class="contact-row"><span class="ico-box"></span>LipoweZacisze.pl</div></div>
<div class="abs fcol" style="left:760px;top:4368px"><h5>Follow us</h5>
  <div class="contact-row"><span class="ico-box"></span>LUMENFEED</div>
  <div class="contact-row"><span class="ico-box"></span>SNAPWALL</div>
  <div class="contact-row"><span class="ico-box"></span>CHIRPLINE</div></div>
<div class="abs fcol" style="left:893px;top:4368px"><h5>Newsletter signup</h5></div>
<div class="abs" style="left:896px;top:4400px;width:182px;height:38px;border:1px solid #fff;border-radius:20px;padding:0 16px;display:flex;align-items:center;font-size:10px;color:#fff">Email</div>
<div class="btn btn-gold" style="left:896px;top:4448px;width:182px;height:36px">Subscribe</div>
<div class="abs" style="left:122px;top:4570px;width:956px;height:1px;background:#555"></div>
<div class="abs" style="left:0;width:1200px;top:4590px;text-align:center;font-size:9px;color:#fff">© 2022 Linden Studio. All rights reserved.</div>

</body>
</html>
```